Create a Magazine Ad for an asbestos law firm

we need an 8 X 13 ad to be on the back of a magazine cover. We have the text Attached and want a similar look and feel to our website : www.claimsharbor-help.com. The ad should be targeted to white males 55 years or older who are conservative and worked in industry or industrial plants. The main offer is a free case review and trying to get them to call the telephone number.

Target Market(s)

White collar men who worked in industrial plants. Age 55 years or older.

Industry/Entity Type

Legal

Requirements
Must have
• Pictures of white middle class conservative man or man and woman
Nice to have
• look at www.claimsharbor-help.com to an. idea of what we are looking for

```html
<!DOCTYPE html>
<html lang="en">
<head>
<meta charset="utf-8">
<title>Mesothelioma Compensation – Magazine Ad</title>
<link rel="stylesheet" href="https://fonts.googleapis.com/css2?family=Poppins:wght@400;500;600;700;800&family=Oswald:wght@600;700&display=swap">
<style>
  :root {
    --ink: #172a33;
    --teal: #6b9ea8;
    --teal-dark: #4f8590;
    --yellow: #f7e11b;
    --white: #ffffff;
    --skin: #f29a78;
    --text: #1b1b1b;
  }
  * { margin: 0; padding: 0; box-sizing: border-box; }
  html, body { width: 770px; height: 1200px; overflow: hidden; background: var(--white); }
  body { font-family: "Poppins", sans-serif; color: var(--text); }
  .ad { position: relative; width: 770px; height: 1200px; background: var(--white); }
  .abs { position: absolute; }

  .hero { left: 0; top: 0; width: 770px; height: 251px; background: var(--ink); }
  .headline { left: 48px; top: 44px; color: var(--white); font-weight: 800; line-height: 1; letter-spacing: -0.5px; }
  .headline span { display: block; }
  .headline .l1 { font-size: 41px; }
  .headline .l2 { font-size: 47px; color: var(--yellow); margin-top: 4px; }
  .headline .l3 { font-size: 47px; margin-top: 3px; }
  .headline .l4 { font-size: 33px; margin-top: 2px; }
  .headline .hl { color: var(--yellow); }
  .hero-figure { left: 512px; top: 18px; width: 212px; height: 233px; border-radius: 90px 90px 0 0;
    background: linear-gradient(180deg, #f4a27f 0%, #ee8f6c 60%, #c9413d 100%); }

  .intro-band { left: 0; top: 251px; width: 770px; height: 74px; background: var(--teal); }
  .intro-text { left: 48px; top: 259px; width: 440px; color: var(--white); font-size: 13.2px; line-height: 18px; }
  .eval-label { left: 547px; top: 264px; color: var(--ink); font-weight: 700; font-size: 17px; }
  .eval-phone { left: 547px; top: 286px; color: var(--yellow); font-weight: 800; font-size: 18.5px; display: flex; align-items: center; gap: 4px; }

  .source { display: flex; align-items: center; gap: 14px; top: 346px; }
  .source .dot { width: 46px; height: 46px; border-radius: 50%; background: var(--ink); border: 3px solid var(--teal); display: flex; align-items: center; justify-content: center; }
  .source .label { font-weight: 700; font-size: 11.5px; line-height: 15px; color: var(--ink); }

  .qualify { left: 83px; top: 410px; font-weight: 700; font-size: 14.6px; color: var(--ink); }
  .checks { left: 89px; top: 438px; list-style: none; font-size: 13.6px; }
  .checks li { display: flex; align-items: center; gap: 14px; height: 19.5px; }
  .checks .tick { width: 10px; height: 10px; border-radius: 50%; background: var(--teal); flex: none; }

  .fund-amount { left: 191px; top: 516px; font-weight: 800; font-size: 38px; color: var(--ink); line-height: 1; }
  .fund-sub { left: 192px; top: 559px; font-weight: 700; font-size: 15.5px; line-height: 17px; color: var(--teal); }
  .fund-body { left: 192px; top: 596px; width: 248px; font-size: 10.2px; line-height: 14px; text-align: justify; color: var(--text); }
  .rule-v { border-left: 1.5px dotted var(--ink); }
  .examples-title { left: 490px; top: 524px; width: 240px; font-weight: 700; font-size: 16.5px; line-height: 20px; color: var(--teal); }
  .examples-note { left: 490px; top: 584px; width: 240px; font-size: 11.6px; line-height: 17.5px; color: var(--text); }

  .case { width: 200px; text-align: center; top: 692px; }
  .case .badge { position: relative; width: 92px; height: 92px; margin: 0 auto; }
  .case .amount { margin-top: 14px; font-weight: 800; font-size: 30px; line-height: 1; color: var(--ink); letter-spacing: -0.5px; }
  .case .note { margin-top: 6px; font-weight: 700; font-size: 11.3px; line-height: 15px; color: var(--ink); }

  .navy-amount { top: 890px; font-family: "Oswald", sans-serif; font-weight: 700; font-size: 55px; line-height: 1; color: var(--ink); letter-spacing: -0.5px; }
  .navy-note { top: 957px; font-weight: 700; font-size: 17px; line-height: 22px; color: var(--ink); }

  .talc-amount { left: 190px; top: 1021px; font-weight: 800; font-size: 30px; line-height: 1; color: var(--ink); }
  .talc-note { left: 190px; top: 1054px; font-weight: 700; font-size: 14.5px; line-height: 19px; color: var(--ink); }
  .eligible { left: 475px; top: 1023px; width: 250px; font-size: 10.4px; line-height: 14.5px; color: var(--text); }

  .cta { left: 98px; top: 1112px; width: 575px; height: 32px; border-radius: 16px; background: var(--teal);
    display: flex; align-items: center; justify-content: center; color: var(--white); font-weight: 700; font-size: 22px; }
  .cta .num { color: var(--yellow); margin-left: 6px; }
  .firm { left: 0; top: 1150px; width: 770px; text-align: center; font-weight: 600; font-size: 10.5px; color: var(--ink); }
</style>
</head>
<body>
<main class="ad">
  <section class="hero abs"></section>
  <h1 class="headline abs">
    <span class="l1">DIAGNOSED WITH</span>
    <span class="l2">MESOTHELIOMA</span>
    <span class="l3">YOU COULD BE</span>
    <span class="l4">OWED <span class="hl">COMPENSATION</span></span>
  </h1>
  <div class="hero-figure abs" role="img" aria-label="Illustration of a person in profile with the airway and lungs shown"></div>

  <section class="intro-band abs"></section>
  <p class="intro-text abs">It's very likely you developed this disease through asbestos exposure. Mesothelioma patients are getting multi-million dollar settlements, decades later, from:</p>
  <p class="eval-label abs">FREE EVALUATION</p>
  <p class="eval-phone abs">
    <svg width="12" height="12" viewBox="0 0 24 24"><path fill="#172a33" d="M6.6 10.8a15 15 0 0 0 6.6 6.6l2.2-2.2c.3-.3.7-.4 1-.2 1.1.4 2.3.6 3.6.6.6 0 1 .4 1 1V20c0 .6-.4 1-1 1A17 17 0 0 1 3 4c0-.6.4-1 1-1h3.5c.6 0 1 .4 1 1 0 1.3.2 2.5.6 3.6.1.3 0 .7-.2 1z"/></svg>
    1-800-555-3001
  </p>

  <div class="source abs" style="left:48px">
    <div class="dot"><svg width="22" height="22" viewBox="0 0 24 24" fill="none" stroke="#fff" stroke-width="1.4"><path d="M12 3v8M12 11c-2 0-3 2-5 3s-3 5-2 6 4 0 5-2 2-4 2-7M12 11c2 0 3 2 5 3s3 5 2 6-4 0-5-2-2-4-2-7"/></svg></div>
    <p class="label">ASBESTOS PRODUCTS<br>EXPOSURE</p>
  </div>
  <div class="source abs" style="left:294px">
    <div class="dot"><svg width="22" height="22" viewBox="0 0 24 24" fill="none" stroke="#fff" stroke-width="1.4"><circle cx="8" cy="7" r="2.5"/><circle cx="16" cy="7" r="2.5"/><circle cx="12" cy="11" r="2.5"/><path d="M4 20v-4c0-2 2-3 4-3M20 20v-4c0-2-2-3-4-3M8 21v-3c0-2 2-3 4-3s4 1 4 3v3"/></svg></div>
    <p class="label" style="font-size:12.5px;line-height:18px">WORKPLACE<br>EXPOSURE</p>
  </div>
  <div class="source abs" style="left:530px">
    <div class="dot"><svg width="20" height="22" viewBox="0 0 20 24" fill="none" stroke="#fff" stroke-width="1.4"><rect x="6" y="2" width="8" height="3"/><rect x="3" y="5" width="14" height="17" rx="2"/><rect x="5" y="10" width="10" height="6"/></svg></div>
    <p class="label">USING BRIGHTVALE TALCUM<br>BABY POWDER</p>
  </div>

  <h2 class="qualify abs">WE CAN HELP YOU FIND OUT IF YOU QUALIFY FOR A CASE IN MINUTES.</h2>
  <ul class="checks abs">
    <li><span class="tick"></span>We'll analyze your situation at no cost</li>
    <li><span class="tick"></span>Determine how much compensation you could be entitled too</li>
    <li><span class="tick"></span>Show you the next steps to get what you're owed</li>
  </ul>

  <svg class="abs" style="left:48px;top:547px" width="116" height="98" viewBox="0 0 116 98">
    <g fill="#6b9ea8"><rect x="0" y="55" width="60" height="10" rx="5"/><rect x="0" y="70" width="60" height="10" rx="5"/><rect x="48" y="30" width="66" height="11" rx="5"/><rect x="48" y="46" width="66" height="11" rx="5"/><rect x="48" y="62" width="66" height="11" rx="5"/><rect x="48" y="78" width="66" height="12" rx="6"/></g>
    <ellipse cx="30" cy="45" rx="30" ry="12" fill="#172a33"/><rect x="0" y="45" width="60" height="8" fill="#172a33"/>
    <ellipse cx="81" cy="14" rx="33" ry="14" fill="#172a33"/><rect x="48" y="14" width="66" height="12" fill="#172a33"/>
  </svg>
  <p class="fund-amount abs">$30 BILLION</p>
  <p class="fund-sub abs">IS AVAILABLE IN TRUST FOR<br>MESOTHELIOMA PATIENTS</p>
  <p class="fund-body abs">Whether you developed Mesothelioma yourself due to asbestos exposure or you're the surviving family of a lost loved one you could be entitled to significant compensation.</p>
  <div class="rule-v abs" style="left:465px;top:524px;height:145px"></div>
  <h2 class="examples-title abs">HOW MUCH MONEY CAN PEOPLE RECEIVE FROM A MESOTHELIOMA CASE?</h2>
  <p class="examples-note abs">BELOW EXAMPLES ARE WHAT CLIENTS RECEIVED AFTER ATTORNEYS FEES &amp; EXPENSES ARE * DEDUCTED.</p>

  <div class="rule-v abs" style="left:264px;top:692px;height:173px"></div>
  <div class="rule-v abs" style="left:502px;top:692px;height:173px"></div>

  <div class="case abs" style="left:47px">
    <div class="badge"><svg width="92" height="92" viewBox="0 0 92 92"><path d="M4 46a42 42 0 0 1 84 0" fill="none" stroke="#172a33" stroke-width="3"/><circle cx="46" cy="48" r="40" fill="#6b9ea8"/><path d="M26 52v-6l6-2 5-7h17l7 7 6 1v7z" fill="#fff"/><circle cx="34" cy="53" r="4" fill="#6b9ea8" stroke="#fff" stroke-width="2"/><circle cx="58" cy="53" r="4" fill="#6b9ea8" stroke="#fff" stroke-width="2"/><path d="M39 39h6v5h-9zM48 39h5l4 5h-9z" fill="#6b9ea8"/></svg></div>
    <p class="amount">$6,142,500</p>
    <p class="note">Exposed through heavy duty<br>vehicles</p>
  </div>
  <div class="case abs" style="left:284px">
    <div class="badge"><svg width="92" height="92" viewBox="0 0 92 92"><path d="M4 46a42 42 0 0 1 84 0" fill="none" stroke="#172a33" stroke-width="3"/><circle cx="46" cy="48" r="40" fill="#6b9ea8"/><path d="M31 28h20l8 8v32H31z" fill="#fff"/><g stroke="#6b9ea8" stroke-width="2.5"><path d="M36 40h12M36 46h16M36 52h12M36 58h10"/></g><path d="M50 62l14-14 4 4-14 14h-4z" fill="#fff" stroke="#6b9ea8" stroke-width="1.5"/></svg></div>
    <p class="amount">$6,033,510</p>
    <p class="note">Exposed through general<br>contracting</p>
  </div>
  <div class="case abs" style="left:516px">
    <div class="badge"><svg width="92" height="92" viewBox="0 0 92 92"><path d="M4 46a42 42 0 0 1 84 0" fill="none" stroke="#172a33" stroke-width="3"/><circle cx="46" cy="48" r="40" fill="#6b9ea8"/><g stroke="#fff" stroke-width="5" stroke-linecap="round"><path d="M32 34l28 28"/><path d="M60 34L34 60"/></g><circle cx="31" cy="33" r="6" fill="#fff"/><circle cx="31" cy="33" r="2.5" fill="#6b9ea8"/><path d="M58 28l8 8-4 2-6-6z" fill="#fff"/></svg></div>
    <p class="amount">$5,939,010</p>
    <p class="note">Exposed through boat repair</p>
  </div>

  <p class="navy-amount abs" style="left:48px">$3,921,750</p>
  <p class="navy-note abs" style="left:48px">Exposed through navy<br>service</p>
  <svg class="abs" style="left:346px;top:898px" width="92" height="88" viewBox="0 0 92 88">
    <rect x="22" y="0" width="28" height="8" fill="#6b9ea8"/>
    <rect x="14" y="10" width="44" height="18" fill="#6b9ea8"/>
    <path d="M4 40l32-14 32 14-8 40H14z" fill="#172a33"/>
    <path d="M10 40l26-10 26 10-4 6-22-8-22 8z" fill="#6b9ea8"/>
    <g fill="none" stroke="#6b9ea8" stroke-width="4"><circle cx="64" cy="44" r="5"/><path d="M64 49v34M54 58h20M46 68a18 18 0 0 0 36 0"/></g>
    <path d="M0 84h10" stroke="#6b9ea8" stroke-width="3"/>
  </svg>
  <p class="navy-amount abs" style="left:493px">$3,600,450</p>
  <p class="navy-note abs" style="left:493px">Exposed through navy<br>service</p>

  <svg class="abs" style="left:98px;top:1018px" width="56" height="72" viewBox="0 0 56 72">
    <rect x="10" y="0" width="22" height="10" rx="3" fill="#6b9ea8"/>
    <rect x="2" y="12" width="38" height="58" rx="8" fill="#6b9ea8"/>
    <circle cx="21" cy="36" r="10" fill="#fff"/>
    <path d="M21 42l-5-5a3 3 0 0 1 5-4 3 3 0 0 1 5 4z" fill="#172a33"/>
    <rect x="15" y="50" width="12" height="4" rx="2" fill="#fff"/>
    <path d="M28 70c4-10 8-14 12-14s10 6 16 14z" fill="#172a33"/>
  </svg>
  <p class="talc-amount abs">$2.5 MILLION</p>
  <p class="talc-note abs">Exposure from Brightvale Talcum<br>Baby Powder</p>
  <p class="eligible abs">Find out if you're Eligible, for FREE, in Minutes. We'll evaluate your situation and tell you what your case could be worth.</p>

  <p class="cta abs">Free evaluation call <span class="num">1-800-555-3000</span></p>
  <p class="firm abs">Martin Hale, Attorney Houston, TX</p>
</main>
</body>
</html>
```